Stationery Design Project

We are a packaging machinery manufacturer that mainly serve the food industry.
We now require a full set of stationary including name card, envelop, letter paper, and etc. to match our company image. The logo has been awarded in a previous contest which is attached here.
Updates
Project Deadline Extended
Reason: We have extended the deadline. We have adjusted the deadline before launch to avoid confusion but it turns out the new date wasn't implemented by the system. All designers please feel free to submit your design. Thank you!
Target Market(s)
B2B customer, including decision maker in food factories, chemical factories, etc.
Industry/Entity Type
Industry
Colors
Designer to choose colors to be used in the design.
Look and feel
Each slider illustrates characteristics of the customer's brand and the style your logo design should communicate.

```html
<!DOCTYPE html>
<html lang="en">
<head>
<meta charset="utf-8">
<title>Norvale Packaging Technology – Envelope Set</title>
<link rel="stylesheet" href="https://fonts.googleapis.com/css2?family=Open+Sans:wght@400;700&display=swap">
<style>
  :root {
    --brand-green: #0e6e41;
    --brand-grey: #838c92;
    --paper: #ffffff;
    --backdrop: #ececec;
    --text-muted: #555b60;
  }
  * { margin: 0; padding: 0; box-sizing: border-box; }
  html, body {
    width: 1200px;
    height: 892px;
    overflow: hidden;
    background: var(--backdrop);
    font-family: "Open Sans", Arial, sans-serif;
  }
  .stationery {
    position: relative;
    width: 1200px;
    height: 892px;
  }
  .envelope {
    position: absolute;
    width: 540px;
    height: 256px;
    background: var(--paper);
    box-shadow: 0 2px 0 #dcdcdc, 0 4px 0 #e4e4e4, 0 10px 22px rgba(0,0,0,0.12);
    overflow: hidden;
  }
  /* Front of envelope */
  .envelope--front { left: 60px; top: 470px; }
  .brand {
    position: absolute;
    left: 26px;
    top: 24px;
    color: var(--brand-green);
    font-weight: 700;
    line-height: 1.05;
  }
  .brand__name { display: block; font-size: 34px; letter-spacing: 1px; }
  .brand__tagline { display: block; font-size: 11.5px; letter-spacing: 1.6px; }
  .brand__dot {
    display: inline-block;
    width: 26px; height: 26px;
    background: var(--brand-green);
    margin-right: 8px;
    vertical-align: -2px;
  }
  .sender-address {
    position: absolute;
    left: 26px;
    top: 118px;
    font-size: 9px;
    color: var(--text-muted);
  }
  .front-band {
    position: absolute;
    left: 0; right: 0; bottom: 0;
    height: 22px;
    display: flex;
  }
  .front-band__grey { width: 44%; background: var(--brand-grey); }
  .front-band__green { flex: 1; background: var(--brand-green); margin-left: 4px; }

  /* Back of envelope */
  .envelope--back { left: 600px; top: 170px; }
  .flap {
    position: absolute;
    left: 0; right: 0; top: 0;
    height: 62px;
    background: var(--brand-green);
    border-top-left-radius: 26px;
    border-bottom-right-radius: 26px;
  }
  .flap__mark {
    position: absolute;
    left: 50%; top: 50%;
    width: 24px; height: 24px;
    margin: -12px 0 0 -12px;
    background: var(--brand-grey);
  }
</style>
</head>
<body>
  <main class="stationery">
    <section class="envelope envelope--back" aria-label="Envelope back">
      <div class="flap"><span class="flap__mark"></span></div>
    </section>

    <section class="envelope envelope--front" aria-label="Envelope front">
      <div class="brand">
        <span class="brand__name"><span class="brand__dot"></span>NORVALE</span>
        <span class="brand__tagline">PACKAGING TECHNOLOGY</span>
      </div>
      <p class="sender-address">street name, city name, state zip code</p>
      <div class="front-band">
        <div class="front-band__grey"></div>
        <div class="front-band__green"></div>
      </div>
    </section>
  </main>
</body>
</html>
```